nutrition company business card

I would like to have a business card that has two sides, one being the green color from the Company name on the logo. I am open to ideas and looks that work with my logo. I like the idea of having a negative image of the tree on the green side.

For my information on the card I must have:
Linda Moorcombe
415-872-6041
lindamoorcombe@quellmail.net

This area will need to be updated once I complete my schooling.

Reason: I need to extend my deadline by one day as I have been sick the last week and not had time to review all the new designs. Thank you.

Industry/Entity Type

Nutrition

Requirements
Must have
• I would like to have a business card that has two sides, one being the green color from the Company name on the logo. I am open to ideas and looks that work with my logo. I like the idea of having a negative image of the tree on the green side.
• For my information on the card I must have:
• Linda Moorcombe
• 415-872-6041
• lindamoorcombe@quellmail.net
• This area will need to be updated once I complete my schooling.

```html
<!DOCTYPE html>
<html lang="en">
<head>
<meta charset="utf-8">
<title>Greenleaf Households – Business Card</title>
<link rel="stylesheet" href="https://fonts.googleapis.com/css2?family=Questrial&family=Montserrat:wght@700&display=swap">
<style>
  :root {
    --brand-green: #84ff00;
    --leaf-tint: #dcfbb8;
    --trunk-tint: #e2e0dc;
    --ink: #5b5e54;
    --paper: #ffffff;
    --backdrop: #ecece8;
  }
  * { margin: 0; padding: 0; box-sizing: border-box; }
  html, body { width: 1200px; height: 1000px; overflow: hidden; background: var(--backdrop); }
  .canvas { position: relative; width: 1200px; height: 1000px; }

  .card {
    position: absolute;
    left: 210px;
    width: 780px;
    height: 440px;
    border-radius: 30px;
    overflow: hidden;
    box-shadow: 0 6px 18px rgba(0,0,0,0.12);
  }

  /* Front side */
  .card--front { top: 40px; background: var(--brand-green); color: var(--paper); }
  .brand-mark {
    position: absolute; left: 50%; top: 48px; transform: translateX(-50%);
    width: 170px; height: 170px; border: 8px solid var(--paper); border-radius: 50%;
  }
  .brand-name {
    position: absolute; left: 0; right: 0; top: 250px; text-align: center;
    font-family: "Questrial", sans-serif; font-size: 64px; letter-spacing: 1px; line-height: 1;
  }
  .brand-tagline {
    position: absolute; left: 0; right: 0; top: 330px; text-align: center;
    font-family: "Questrial", sans-serif; font-size: 34px; letter-spacing: 3px; line-height: 1;
  }

  /* Back side */
  .card--back { top: 520px; background: var(--paper); color: var(--ink); }
  .backdrop-decor {
    position: absolute; left: 150px; top: 0; width: 600px; height: 440px;
    background:
      radial-gradient(ellipse 40% 45% at 50% 55%, var(--trunk-tint) 0%, rgba(226,224,220,0) 70%),
      radial-gradient(ellipse 70% 60% at 55% 35%, var(--leaf-tint) 0%, rgba(220,251,184,0) 75%);
    opacity: 0.9;
  }
  .contact-name {
    position: absolute; left: 200px; top: 120px;
    font-family: "Montserrat", sans-serif; font-weight: 700; font-size: 52px; letter-spacing: 1px;
  }
  .contact-line {
    position: absolute; display: flex; align-items: center; gap: 10px;
    font-family: "Questrial", sans-serif; font-size: 28px;
  }
  .contact-line svg { width: 22px; height: 26px; flex: none; }
  .contact-line--phone { left: 40px; top: 250px; }
  .contact-line--email { right: 30px; top: 300px; }
  .notice-band {
    position: absolute; left: 0; right: 0; top: 345px; height: 44px;
    background: var(--brand-green); color: var(--paper);
    font-family: "Questrial", sans-serif; font-size: 24px; line-height: 44px; text-align: center;
  }
</style>
</head>
<body>
<main class="canvas">
  <section class="card card--front" aria-label="Front of card">
    <div class="brand-mark" aria-hidden="true"></div>
    <h1 class="brand-name">Greenleaf Households</h1>
    <p class="brand-tagline">healthy eating made easy</p>
  </section>

  <section class="card card--back" aria-label="Back of card">
    <div class="backdrop-decor" role="img" aria-label="Faint tree with light green leaves as background decoration"></div>
    <h2 class="contact-name">Linda Moorcombe</h2>
    <p class="contact-line contact-line--phone">
      <svg viewBox="0 0 22 26" aria-hidden="true"><rect x="4" y="1" width="14" height="24" rx="3" fill="none" stroke="currentColor" stroke-width="2"/><line x1="9" y1="21" x2="13" y2="21" stroke="currentColor" stroke-width="2"/></svg>
      415-872-6041
    </p>
    <p class="contact-line contact-line--email">
      lindamoorcombe@quellmail.net
      <svg viewBox="0 0 22 26" aria-hidden="true"><rect x="1" y="7" width="20" height="13" fill="none" stroke="currentColor" stroke-width="1.6"/><polyline points="1,7 11,15 21,7" fill="none" stroke="currentColor" stroke-width="1.6"/></svg>
    </p>
    <p class="notice-band">This area will need to be updated once I complete my schooling</p>
  </section>
</main>
</body>
</html>
```